Dinewell - Slate App Design Project

I have a Slate app that serves as a restaurant reservation system. The design that i currently have is very basic apple design. I am looking for it to have a much more professional appeal.

Please review the attached document which contains all of the screen shots for the app.
Updates

This Project has now been Guaranteed.  I look forward to reviewing your designs.

Brent

Reason: I am extending my deadline because i just changed this contest to guaranteed and have received a ton more "acceptances" because of it and I want to give those designers a chance to submit a design.

Target Market(s)

restaurant owners

Industry/Entity Type

Restaurant

Requirements
Must have
• On the seating chart i am changing the feature that shows the tables highlighted and instead would like that replace with a badge. So the list of wait staff across the top of the seating chart would instead have a number next to their name and would correspond with the badge on the table to determine their section.

So for example:
Ada would have a number 1 in front of her name and tables 18, 19, 20, and 31 would have a little badge in the upper right hand corner with the number "1" inside the badge.
Uma would have a number 2 in front of her name and tables 6, 7, and 11 would have a little badge in the upper right hand corner with the number " 2" inside the badge.
Nora would have a number 3 in front of her name and tables 12, 13, 27, 28, 29, and 30 would have a little badge in the upper right hand corner with the number " 3" inside the badge.

The names on the top will all be ONE color

Also, i would like an icon developed to replace the "C" you see next to some of the people's name in the reservation and waitlist slots. Also, i would like a better looking "check mark".

```html
<!DOCTYPE html>
<html lang="en">
<head>
<meta charset="utf-8">
<title>Dinewell – Reservations</title>
<link href="https://fonts.googleapis.com/css2?family=Arimo:ital,wght@0,400;0,700;1,400;1,700&display=swap" rel="stylesheet">
<style>
:root{
  --ink:#3d3d3d;
  --ink-soft:#555;
  --blue:#2f7fd6;
  --blue-dark:#1f63b3;
  --blue-text:#2a6fd6;
  --brown:#b0650f;
  --orange:#c9690d;
  --badge-gray:#8b8b8b;
  --wait-bg:#fcf5d8;
  --wait-head:#f5e3a2;
  --open-head:#d8dbfb;
  --open-row:#e7ecf8;
  --full-head:#c9c9c9;
  --full-row:#ececec;
  --plain-row:#f6f6f6;
  --line:#d4d4d4;
  --header-bg:#ffffff;
}
*{box-sizing:border-box;margin:0;padding:0}
html,body{width:1200px;height:900px;overflow:hidden;background:#fff}
body{font-family:"Arimo",Helvetica,Arial,sans-serif;color:var(--ink);position:relative}

.status-bar{height:22px;background:#000;color:#fff;font-size:14px;display:flex;align-items:center;justify-content:space-between;padding:0 6px;position:relative}
.status-bar .time{position:absolute;left:0;right:0;text-align:center;font-weight:700}
.status-bar .left,.status-bar .right{display:flex;align-items:center;gap:5px}
.battery{width:24px;height:11px;border:1.5px solid #fff;border-radius:2px;padding:1px}
.battery i{display:block;height:100%;background:#fff}

.app-header{height:75px;background:var(--header-bg);border-bottom:1px solid var(--line);position:relative}
.brand{position:absolute;left:12px;top:8px;display:flex;align-items:center;gap:8px}
.brand-mark{width:22px;height:22px;background:#9aa6b4;border-radius:3px}
.brand-name{font-size:25px;color:#8d9aa9;font-weight:400;letter-spacing:-.5px}
.greeting{position:absolute;left:152px;top:12px;font-size:21px;font-weight:700;color:var(--blue-text)}
.stats{position:absolute;left:12px;top:44px;display:flex;gap:12px;color:var(--brown);font-size:19px;font-weight:700}
.stat{display:flex;align-items:center;gap:3px}
.stat svg{width:20px;height:20px;fill:var(--brown)}
.nav{position:absolute;right:12px;top:3px;display:flex;gap:7px}
.nav-btn{height:37px;padding:0 14px;border-radius:6px;background:linear-gradient(#4aa3ee,#1f72c9);color:#fff;font-size:21px;font-weight:700;display:flex;align-items:center;box-shadow:0 2px 2px rgba(0,0,0,.3);border:1px solid #1a5ea8}
.nav-btn.is-muted{background:linear-gradient(#c8e3f8,#8cbfe8);border-color:#86b3d8}

.board{position:absolute;top:97px;left:0;width:1200px;height:803px;display:flex}
.column{width:400px;height:100%;overflow:hidden;border-right:1px solid #b9b9b9}
.column:last-child{border-right:none}
.waitlist{background:var(--wait-bg)}

.slot-head{height:44px;display:flex;align-items:center;padding:0 12px;font-size:21px;font-weight:700;border-bottom:1px solid var(--line);position:relative}
.slot-head .avail{position:absolute;left:181px}
.slot-head .avail.is-wide{left:203px}
.slot-head.is-open{background:linear-gradient(#e4e6fd,var(--open-head));color:var(--blue-text)}
.slot-head.is-full{background:linear-gradient(#d6d6d6,var(--full-head));color:var(--ink-soft)}
.slot-head.is-wait{background:linear-gradient(#f9ecb9,var(--wait-head));color:#8a5a10}
.add{position:absolute;right:10px;top:12px;width:20px;height:20px;fill:none;stroke:var(--blue);stroke-width:3.5}
.is-wait .add{stroke:var(--orange)}

.row{height:46px;padding:0 48px 0 12px;display:flex;flex-direction:column;justify-content:center;border-bottom:1px solid var(--line);position:relative}
.row.has-note{height:60px}
.open .row{background:var(--open-row)}
.full .row{background:var(--full-row)}
.full.light .row{background:var(--plain-row)}
.waitlist .row{height:47px;background:var(--wait-bg)}
.line{display:flex;align-items:center;gap:5px}
.name{font-size:21px;font-weight:700;color:var(--ink);margin-left:4px}
.note{font-size:12px;font-style:italic;font-weight:700;color:#555;margin-top:2px}

.badge{height:24px;border-radius:4px;display:inline-flex;align-items:center;gap:3px;padding:0 5px;color:#fff;font-size:15px;font-weight:700}
.badge svg{width:17px;height:17px;fill:#fff}
.badge.party{background:linear-gradient(#a5a5a5,var(--badge-gray))}
.badge.wait{background:linear-gradient(#4fa5ee,var(--blue))}
.badge.wait svg{fill:none;stroke:#fff;stroke-width:2}
.badge.table{background:linear-gradient(#d97c1e,var(--orange));font-size:16px}
.alert{width:24px;height:24px;border-radius:50%;background:linear-gradient(#4aa5ef,var(--blue-dark));color:#fff;font-size:17px;font-weight:700;display:inline-flex;align-items:center;justify-content:center}
.check{position:absolute;right:12px;top:50%;width:26px;height:26px;margin-top:-13px}
</style>
</head>
<body>
<svg width="0" height="0" style="position:absolute" aria-hidden="true">
  <defs>
    <symbol id="i-person" viewBox="0 0 20 20"><circle cx="10" cy="6" r="4"/><path d="M2 19c0-5 3.5-7.5 8-7.5s8 2.5 8 7.5z"/></symbol>
    <symbol id="i-group" viewBox="0 0 24 20"><circle cx="9" cy="6" r="4"/><circle cx="16" cy="5" r="3.5"/><path d="M1 19c0-5 3.5-7.5 8-7.5s8 2.5 8 7.5z"/><path d="M15 10.5c4 0 8 2 8 7h-5c0-3-1-5-3-7z"/></symbol>
    <symbol id="i-clock" viewBox="0 0 20 20"><circle cx="10" cy="10" r="8"/><path d="M10 5v5l3.5 2"/></symbol>
    <symbol id="i-clock-solid" viewBox="0 0 20 20"><path d="M10 1a9 9 0 1 0 0 18a9 9 0 1 0 0-18zm0 2.2a6.8 6.8 0 1 1 0 13.6a6.8 6.8 0 1 1 0-13.6zM9 5v6l4.5 2.6l.9-1.5L11 10.2V5z"/></symbol>
    <symbol id="i-table" viewBox="0 0 22 20"><path d="M1 5h20v3H1zM3 8h2v11H3zM17 8h2v11h-2zM2 2h3v3H2zM17 2h3v3h-3z"/></symbol>
    <symbol id="i-check" viewBox="0 0 26 26"><circle cx="13" cy="13" r="12" fill="#2f86dc"/><path d="M7 13.5l4 4 8-9" fill="none" stroke="#fff" stroke-width="3" stroke-linecap="round" stroke-linejoin="round"/></symbol>
    <symbol id="i-add" viewBox="0 0 20 20"><path d="M10 2v16M2 10h16"/></symbol>
  </defs>
</svg>

<div class="status-bar">
  <div class="left"><span>Slate</span>
    <svg width="15" height="11" viewBox="0 0 15 11"><path d="M7.5 10L5 7.5a3.5 3.5 0 0 1 5 0zM2.5 5a7 7 0 0 1 10 0l-1.2 1.2a5.3 5.3 0 0 0-7.6 0zM0 2.5a10.6 10.6 0 0 1 15 0l-1.2 1.2a8.9 8.9 0 0 0-12.6 0z" fill="#fff"/></svg>
  </div>
  <span class="time">4:20 PM</span>
  <div class="right"><svg width="13" height="13" viewBox="0 0 20 20"><circle cx="10" cy="10" r="9" fill="#fff"/><path d="M10 5v5l3 2" stroke="#000" stroke-width="2" fill="none"/></svg><div class="battery"><i></i></div></div>
</div>

<header class="app-header">
  <div class="brand"><span class="brand-mark"></span><span class="brand-name">Dinewell</span></div>
  <div class="greeting">Hi Nora!</div>
  <div class="stats">
    <span class="stat"><svg><use href="#i-person"/></svg>56</span>
    <span class="stat"><svg viewBox="0 0 24 20" style="width:24px"><use href="#i-group"/></svg>14</span>
    <span class="stat"><svg><use href="#i-clock-solid"/></svg>25m</span>
    <span class="stat"><svg viewBox="0 0 22 20" style="width:22px"><use href="#i-table"/></svg>11(296)</span>
    <span class="stat"><svg viewBox="0 0 22 20" style="width:22px"><use href="#i-table"/></svg>370</span>
  </div>
  <nav class="nav">
    <span class="nav-btn">Seating Chart</span>
    <span class="nav-btn">Specials</span>
    <span class="nav-btn">Staff Notes</span>
    <span class="nav-btn">Calendar</span>
    <span class="nav-btn is-muted">Management</span>
  </nav>
</header>

<main class="board">
  <section class="column waitlist">
    <div class="slot-head is-wait">Wait List<svg class="add" viewBox="0 0 20 20"><use href="#i-add"/></svg></div>
    <div class="row"><div class="line"><span class="badge wait"><svg><use href="#i-clock"/></svg>5</span><span class="badge party"><svg><use href="#i-person"/></svg>4</span><span class="name">Wren Talbot</span></div></div>
    <div class="row"><div class="line"><span class="badge wait"><svg><use href="#i-clock"/></svg>5</span><span class="badge party"><svg><use href="#i-person"/></svg>2</span><span class="name">Brent Halvorsen</span></div></div>
    <div class="row"><div class="line"><span class="badge wait"><svg><use href="#i-clock"/></svg>25</span><span class="badge party"><svg><use href="#i-person"/></svg>4</span><span class="name">Della Voss</span></div></div>
    <div class="row"><div class="line"><span class="badge wait"><svg><use href="#i-clock"/></svg>25</span><span class="badge party"><svg><use href="#i-person"/></svg>3</span><span class="name">Abril Canto</span></div></div>
    <div class="row"><div class="line"><span class="badge wait"><svg><use href="#i-clock"/></svg>30</span><span class="badge party"><svg><use href="#i-person"/></svg>4</span><span class="name">Marisol Hendry</span></div></div>
    <div class="row"><div class="line"><span class="badge wait"><svg><use href="#i-clock"/></svg>30</span><span class="badge party"><svg><use href="#i-person"/></svg>6</span><span class="name">Jolene Pratt</span></div></div>
    <div class="row"><div class="line"><span class="badge wait"><svg><use href="#i-clock"/></svg>30</span><span class="badge party"><svg><use href="#i-person"/></svg>6</span><span class="name">Juno Bellweather</span></div></div>
    <div class="row"><div class="line"><span class="badge wait"><svg><use href="#i-clock"/></svg>15</span><span class="badge party"><svg><use href="#i-person"/></svg>4</span><span class="name">Noelle Farrow</span></div></div>
    <div class="row"><div class="line"><span class="badge wait"><svg><use href="#i-clock"/></svg>40</span><span class="badge party"><svg><use href="#i-person"/></svg>5</span><span class="name">Jasper Quill</span></div></div>
  </section>

  <section class="column">
    <div class="open">
      <div class="slot-head is-open">12:00 PM<span class="avail is-wide">Open 9(22)</span><svg class="add" viewBox="0 0 20 20"><use href="#i-add"/></svg></div>
      <div class="row has-note"><div class="line"><span class="badge party"><svg><use href="#i-person"/></svg>4</span><span class="badge table">T 11</span><span class="name">Otto Brindle</span></div><p class="note">I would like a booth in the corner</p><svg class="check"><use href="#i-check"/></svg></div>
      <div class="row"><div class="line"><span class="badge party"><svg><use href="#i-person"/></svg>3</span><span class="name">Ada Quillon</span></div><svg class="check"><use href="#i-check"/></svg></div>
      <div class="row has-note"><div class="line"><span class="alert">!</span><span class="badge party"><svg><use href="#i-person"/></svg>2</span><span class="badge table">T 1</span><span class="name">Lyle Dunmore</span></div><p class="note">Patio table if available</p></div>
    </div>
    <div class="full">
      <div class="slot-head is-full">12:15 PM<span class="avail">Full</span></div>
      <div class="row"><div class="line"><span class="badge party"><svg><use href="#i-person"/></svg>4</span><span class="name">Felix Ormond</span></div><svg class="check"><use href="#i-check"/></svg></div>
      <div class="row has-note"><div class="line"><span class="alert">!</span><span class="badge party"><svg><use href="#i-person"/></svg>5</span><span class="badge table">T 12</span><span class="name">Rowan Kestrel</span></div><p class="note">Birthday celebration</p><svg class="check"><use href="#i-check"/></svg></div>
      <div class="row has-note"><div class="line"><span class="badge party"><svg><use href="#i-person"/></svg>2</span><span class="name">Milo Thackery</span></div><p class="note">We have one person that needs gluten free food</p><svg class="check"><use href="#i-check"/></svg></div>
      <div class="row"><div class="line"><span class="badge party"><svg><use href="#i-person"/></svg>4</span><span class="name">Silas Penrose</span></div></div>
    </div>
    <div class="open">
      <div class="slot-head is-open">12:30 PM<span class="avail">Open 12(20)</span><svg class="add" viewBox="0 0 20 20"><use href="#i-add"/></svg></div>
      <div class="row"><div class="line"><span class="badge party"><svg><use href="#i-person"/></svg>4</span><span class="name">Greta Lindqvist</span></div><svg class="check"><use href="#i-check"/></svg></div>
      <div class="row"><div class="line"><span class="badge party"><svg><use href="#i-person"/></svg>5</span><span class="name">Tess Calloway</span></div><svg class="check"><use href="#i-check"/></svg></div>
      <div class="row has-note"><div class="line"><span class="alert">!</span><span class="badge party"><svg><use href="#i-person"/></svg>3</span><span class="name">Gideon Ashcombe</span></div><p class="note">Corner booth</p></div>
      <div class="slot-head is-open">12:45 PM<span class="avail">Open 7(20)</span><svg class="add" viewBox="0 0 20 20"><use href="#i-add"/></svg></div>
      <div class="row"><div class="line"><span class="badge party"><svg><use href="#i-person"/></svg>3</span><span class="name">Hugo Pell</span></div></div>
      <div class="row"><div class="line"><span class="alert">!</span><span class="badge party"><svg><use href="#i-person"/></svg>4</span><span class="name">Omri Vantage</span></div></div>
    </div>
  </section>

  <section class="column">
    <div class="full light">
      <div class="slot-head is-full">1:00 PM<span class="avail">Full</span></div>
      <div class="row has-note"><div class="line"><span class="alert">!</span><span class="badge party"><svg><use href="#i-person"/></svg>4</span><span class="name">&nbsp;Juniper Roe</span></div><p class="note">Quiet table in back</p><svg class="check"><use href="#i-check"/></svg></div>
      <div class="row"><div class="line"><span class="badge party"><svg><use href="#i-person"/></svg>3</span><span class="name">Vesna Lorimer</span></div><svg class="check"><use href="#i-check"/></svg></div>
      <div class="row has-note"><div class="line"><span class="alert">!</span><span class="badge party"><svg><use href="#i-person"/></svg>2</span><span class="badge table">T 1</span><span class="name">Cora Whitlow</span></div><p class="note">Booth please</p></div>
      <div class="row"><div class="line"><span class="badge party"><svg><use href="#i-person"/></svg>3</span><span class="name">Lina Foxley</span></div><svg class="check"><use href="#i-check"/></svg></div>
    </div>
    <div class="open">
      <div class="slot-head is-open">1:15 PM<span class="avail">Open 17(20)</span><svg class="add" viewBox="0 0 20 20"><use href="#i-add"/></svg></div>
      <div class="row"><div class="line"><span class="badge party"><svg><use href="#i-person"/></svg>5</span><span class="name">Ada Merrow</span></div></div>
      <div class="row has-note"><div class="line"><span class="badge party"><svg><use href="#i-person"/></svg>8</span><span class="name">Marlon Ardent</span></div><p class="note">Business meeting</p></div>
      <div class="row"><div class="line"><span class="alert">!</span><span class="badge party"><svg><use href="#i-person"/></svg>4</span><span class="name">Miles Tovey</span></div><svg class="check"><use href="#i-check"/></svg></div>
    </div>
    <div class="full light">
      <div class="slot-head is-full">1:30 PM<span class="avail">Full</span></div>
      <div class="row"><div class="line"><span class="badge party"><svg><use href="#i-person"/></svg>6</span><span class="name">Theo Marchetti</span></div></div>
      <div class="row has-note"><div class="line"><span class="alert">!</span><span class="badge party"><svg><use href="#i-person"/></svg>2</span><span class="name">Maddox Crane</span></div><p class="note">Patio please</p><svg class="check"><use href="#i-check"/></svg></div>
      <div class="row"><div class="line"><span class="badge party"><svg><use href="#i-person"/></svg>6</span><span class="name">Delphine Marbury</span></div></div>
      <div class="row"><div class="line"><span class="badge party"><svg><use href="#i-person"/></svg>2</span><span class="name">Ezra Hollis</span></div></div>
    </div>
    <div class="open">
      <div class="slot-head is-open">1:45 PM<span class="avail">Open 4(20)</span></div>
      <div class="row"><div class="line"><span class="badge party"><svg><use href="#i-person"/></svg>4</span><span class="name">Hal Brennard</span></div></div>
    </div>
  </section>
</main>
</body>
</html>
```